ALL ASPECTS OF PLASTERING INC: TEXTURE,SANDFINISH RENO,POOLS, PATCH WORK ( STATEWIDE SERVICE GOOD RATES) 100% GUARANTEED FULLY INSURED C

Target Market(s)

ANYONE WHO OWNS A HOUSE,BUILDERS

Industry/Entity Type

Work

Contact Information for Business Card

KLAY-TOPP PLASTERING SERVICES
GERALD PETRAKIS 0438916247
EMAIL:VORTAKE58@QUENMAIL.COM

Requirements
Must have
• COLOUR BACKGROUND WIV PLASTERING PICTURE EG TROWEL, CEMENT MIXER, SAND
Nice to have
• BOLD PROFESSIONAL LOOKING AND SOUNDING CATCHY SAYING
Should not have
• FLURO COLOURS

```html
<!DOCTYPE html>
<html lang="en">
<head>
<meta charset="utf-8">
<title>Klay-Topp Plastering Services – Business Card</title>
<link rel="stylesheet" href="https://fonts.googleapis.com/css2?family=Montserrat:wght@200;300;600;700&display=swap">
<style>
  :root {
    --page: #ffffff;
    --blue: #2f86bf;
    --pink: #efb1a1;
    --grey-dark: #9c9c9c;
    --grey-mid: #c9c9c9;
    --grey-light: #e4e4e2;
    --yellow: #e3c12c;
    --stucco: #e8e8e8;
    --stucco-edge: #cfcfcf;
    --brick-a: #a3452f;
    --brick-b: #c1654a;
    --brick-c: #8c7f7a;
    --ink: #1d1d1d;
    --white: #ffffff;
  }
  html, body {
    margin: 0;
    padding: 0;
    overflow: hidden;
  }
  body {
    width: 849px;
    height: 1200px;
    background: var(--page);
    position: relative;
    font-family: "Montserrat", Arial, sans-serif;
  }

  /* Front of card */
  .card-front {
    position: absolute;
    left: 129px;
    top: 90px;
    width: 578px;
    height: 357px;
    display: flex;
    overflow: hidden;
  }
  .swatch { height: 100%; }
  .swatch--blue { width: 75px; background: var(--blue); }
  .swatch--pink { width: 85px; background: var(--pink); }
  .swatch--grey-dark { width: 99px; background: var(--grey-dark); }
  .swatch--grey-mid { width: 98px; background: var(--grey-mid); }
  .swatch--grey-light { width: 95px; background: var(--grey-light); }
  .swatch--yellow { flex: 1; background: var(--yellow); }

  .front-text {
    position: absolute;
    left: 34px;
    top: 36px;
    color: var(--white);
  }
  .brand-name {
    margin: 0;
    font-size: 34px;
    font-weight: 600;
    letter-spacing: 1px;
    line-height: 1;
  }
  .brand-tagline {
    margin: 2px 0 0;
    font-size: 17px;
    font-weight: 200;
    letter-spacing: 0.5px;
    padding-bottom: 6px;
    border-bottom: 1.5px solid var(--white);
    width: 256px;
  }
  .person-name {
    margin: 14px 0 0;
    font-size: 19px;
    font-weight: 700;
  }
  .person-phone {
    margin: 2px 0 0;
    font-size: 21px;
    font-weight: 200;
    letter-spacing: 1px;
  }
  .person-email {
    margin: 30px 0 0;
    font-size: 13px;
    font-weight: 600;
  }

  /* Back of card */
  .card-back {
    position: absolute;
    left: 240px;
    top: 515px;
    width: 357px;
    height: 578px;
    overflow: hidden;
  }
  .brick-wall {
    position: absolute;
    inset: 0;
    background: linear-gradient(160deg, var(--brick-b) 0%, var(--brick-a) 45%, var(--brick-c) 75%, var(--brick-a) 100%);
  }
  .stucco-cover {
    position: absolute;
    left: 0;
    top: 0;
  }
  .back-text {
    position: absolute;
    left: 39px;
    top: 54px;
    color: var(--ink);
  }
  .services-intro {
    margin: 0;
    font-size: 11.5px;
    font-weight: 300;
  }
  .services-list {
    margin: 4px 0 0;
    font-size: 16.5px;
    font-weight: 700;
    line-height: 1.35;
  }
  .services-note {
    margin: 1px 0 0;
    font-size: 11px;
    font-weight: 600;
  }
  .guarantee-band {
    position: absolute;
    left: 0;
    top: 480px;
    width: 100%;
    height: 34px;
    background: var(--stucco);
    display: flex;
    align-items: center;
    box-sizing: border-box;
    padding-left: 39px;
    font-size: 12.5px;
    font-weight: 700;
    color: var(--ink);
  }
</style>
</head>
<body>

  <section class="card-front" aria-label="Business card front">
    <div class="swatch swatch--blue"></div>
    <div class="swatch swatch--pink"></div>
    <div class="swatch swatch--grey-dark"></div>
    <div class="swatch swatch--grey-mid"></div>
    <div class="swatch swatch--grey-light"></div>
    <div class="swatch swatch--yellow"></div>

    <div class="front-text">
      <h1 class="brand-name">KLAY-TOPP</h1>
      <p class="brand-tagline">PLASTERING SERVICES</p>
      <p class="person-name">GERALD PETRAKIS</p>
      <p class="person-phone">043 891 6247</p>
      <p class="person-email">e-mail - vortake58@quenmail.com</p>
    </div>
  </section>

  <section class="card-back" aria-label="Business card back">
    <div class="brick-wall" role="img" aria-label="Photo of a weathered red brick wall with a paintbrush spreading plaster over it"></div>

    <svg class="stucco-cover" width="357" height="300" viewBox="0 0 357 300" aria-hidden="true">
      <path d="M0 0 H357 V87 C300 112 232 170 165 228 C120 266 62 290 0 284 Z"
            fill="var(--stucco)" stroke="var(--stucco-edge)" stroke-width="2"/>
    </svg>

    <div class="back-text">
      <p class="services-intro">ALL ASPECTS OF PLASTERING INC:</p>
      <p class="services-list">TEXTURE • SANDFINISH RENO<br>• POOLS • PATCH WORK</p>
      <p class="services-note">(statewide service good rates)</p>
    </div>

    <div class="guarantee-band">100% GUARANTEED FULLY INSURED C</div>
  </section>

</body>
</html>
```